Make it cool to work near where you are...

Calling all creatives - create the ultimate cool card for people who want to cut their commute.

Here at FarlowBench we've got what can best be described as an Quillet card for desks - and we want to brighten up the wallets of our most loyal users.

So, pitch us your ideas and you might see your design on cards being flashed across the country - and we've thrown in a bit of cash too.

Do see our brief card guidelines - with a couple of past examples thrown in.

```html
<!DOCTYPE html>
<html lang="en">
<head>
<meta charset="utf-8">
<title>FarlowBench membership card — front and back</title>
<link rel="stylesheet" href="https://fonts.googleapis.com/css2?family=Montserrat:wght@800&family=Arimo:wght@700&display=swap">
<style>
  :root {
    --page: #bac8c5;
    --card-dark: #262b2d;
    --band-dark: #202527;
    --card-light: #e7ecea;
    --magenta: #f71bcb;
    --white: #ffffff;
  }
  * { margin: 0; padding: 0; box-sizing: border-box; }
  html, body {
    width: 945px;
    height: 1200px;
    overflow: hidden;
    background: var(--page);
  }
  .sheet {
    position: relative;
    width: 945px;
    height: 1200px;
  }
  .card {
    position: absolute;
    left: 66px;
    width: 813px;
    height: 510px;
    border-radius: 16px;
    overflow: hidden;
  }
  .card--front { top: 63px; background: var(--card-dark); }
  .card--back { top: 630px; background: var(--card-light); }

  .card__artwork {
    position: absolute;
    left: 0; top: 0;
    width: 100%;
    height: 412px;
  }
  .card--front .card__artwork {
    background: linear-gradient(100deg, #1c2123 0%, #262c2e 45%, #4a5456 72%, #6f7c7e 100%);
  }
  .card--back .card__artwork {
    background: linear-gradient(100deg, #e3e8e6 0%, #e7ecea 50%, #eef1f0 75%, #f3f5f4 100%);
  }

  .card__band {
    position: absolute;
    left: 0; bottom: 0;
    width: 100%;
    height: 98px;
    background: var(--band-dark);
  }

  .card__name {
    position: absolute;
    left: 157px;
    top: 90px;
    font-family: "Montserrat", sans-serif;
    font-weight: 800;
    font-size: 44px;
    letter-spacing: -1.5px;
    line-height: 1;
    color: var(--magenta);
  }

  .card__number {
    position: absolute;
    left: 53px;
    top: 352px;
    font-family: "Arimo", sans-serif;
    font-weight: 700;
    font-size: 31px;
    letter-spacing: 1px;
    color: var(--white);
  }

  .card__web {
    position: absolute;
    left: 0;
    width: 780px;
    top: 448px;
    text-align: center;
    font-family: "Arimo", sans-serif;
    font-weight: 700;
    font-size: 27px;
    color: var(--white);
  }

  .card__badge {
    position: absolute;
    left: 603px;
    top: 370px;
    width: 162px;
    height: 75px;
    border: 2px solid var(--white);
    border-radius: 8px;
    background: var(--card-dark);
    display: flex;
    align-items: center;
    justify-content: center;
    font-family: "Montserrat", sans-serif;
    font-weight: 800;
    font-size: 21px;
    letter-spacing: -0.5px;
    color: var(--white);
  }
</style>
</head>
<body>
  <main class="sheet">
    <section class="card card--front" aria-label="Card front">
      <div class="card__artwork" role="img" aria-label="Dark world map overlaid with a faceted grey triangle and chevron pattern"></div>
      <div class="card__band"></div>
      <p class="card__name">FarlowBench</p>
      <p class="card__number">0019 821 849 297</p>
      <div class="card__badge">FarlowBench</div>
      <p class="card__web">www.farlowbench.com</p>
    </section>

    <section class="card card--back" aria-label="Card back">
      <div class="card__artwork" role="img" aria-label="Pale faceted triangle and chevron pattern in light greys"></div>
      <div class="card__band"></div>
      <p class="card__name">FarlowBench</p>
      <div class="card__badge">FarlowBench</div>
      <p class="card__web">www.farlowbench.com</p>
    </section>
  </main>
</body>
</html>
```